Clinical Research Consulting Company needs a web design

My consulting company provides service on clinical trial design and clincal research, product safety and claim development strategy, and lecture service.

Need template and graphic design for the website of my consulting company. Website will have many different tabs (e.g., Home, About Us, Service, and Contact Us).

Like to have modern look and easy on eyes (not too many colors).

We don't perform laboratory work so please do not use pictures with people working in the laboratory. Also, the logo is added. Thanks.

Target Market(s)

Pharmaceutical and Biotech companies, dietary supplement companies, food industry

Industry/Entity Type

It Company

Number of Pages Required

4 page

Font styles to use
Sans Serif

Requirements
Must have
• hyperlink to Contact Us page
Nice to have
• pictures

```html
<!DOCTYPE html>
<html lang="en">
<head>
<meta charset="utf-8">
<title>KAIRO Consulting – Clinical Research Consulting</title>
<link href="https://fonts.googleapis.com/css2?family=Open+Sans:wght@400;600;700&display=swap" rel="stylesheet">
<style>
:root{
  --navy:#1f3a93;
  --navy-dark:#22337f;
  --footer:#2a3d94;
  --green:#8dc63f;
  --text:#333333;
  --muted:#555555;
  --band:#f3f3f3;
  --line:#d6d6d6;
  --fb:#8a9bd0;
  --tw:#8fb6e0;
  --yt:#e8877d;
  --foot-icon:#8e9bbd;
}
*{box-sizing:border-box;margin:0;padding:0}
html,body{width:903px;height:1200px;overflow:hidden;background:#fff}
body{position:relative;font-family:"Open Sans",Arial,sans-serif;color:var(--text)}
a{text-decoration:none;color:inherit}
.abs{position:absolute}

/* header */
.site-header{position:absolute;left:0;top:0;width:903px;height:64px;background:#fff;border-bottom:1px solid #e6e6e6}
.brand{position:absolute;left:135px;top:14px;display:flex;align-items:center;gap:7px}
.brand-dot{width:30px;height:30px;border-radius:50%;background:var(--green)}
.brand-name{font-size:15px;font-weight:700;color:var(--navy);line-height:1.1}
.main-nav a{position:absolute;top:24px;font-size:11.5px;color:var(--navy)}
.main-nav a.active{color:var(--green)}
.nav-marker{position:absolute;left:328px;top:62px;width:38px;height:2px;background:var(--green)}
.social-top span{position:absolute;top:21px;width:23px;height:23px;border-radius:50%}

/* hero */
.hero{position:absolute;left:0;top:64px;width:903px;height:387px;
  background:linear-gradient(100deg,#5d8fe8 0%,#6fa8f0 25%,#b9a6e6 45%,#d8c2cf 62%,#e7d2c4 78%,#d9c6bd 100%)}
.hero-text{position:absolute;left:158px;top:100px;text-align:center;color:#fff;text-shadow:0 1px 3px rgba(0,0,0,.35)}
.hero-text .h1{font-size:27px;line-height:30px;font-weight:400}
.hero-text .h2{font-size:22px;line-height:28px;padding-left:45px}
.hero-text .h3{font-size:18px;line-height:24px;padding-left:10px}
.btn{display:inline-block;background:var(--navy);color:#fff;border:1px solid #fff;outline:1px solid var(--navy);font-size:10px;text-align:center}
.hero .btn{position:absolute;left:240px;top:195px;width:90px;height:25px;line-height:23px;font-size:12.5px}
.hero-rule{position:absolute;left:0;top:451px;width:903px;height:1px;background:var(--green)}

/* welcome */
.welcome-title{position:absolute;left:0;top:472px;width:903px;text-align:center;font-size:17px;color:var(--navy)}
.welcome-title small{font-size:13px;color:var(--text)}
.welcome-title b{font-weight:600}
.welcome-title .accent{color:var(--green)}
.title-rule{position:absolute;height:1px;background:var(--line)}
.welcome-img{position:absolute;left:135px;top:510px;width:155px;height:128px;background:linear-gradient(135deg,#9fc4ec,#3b6fd0 60%,#e6eef8)}
.welcome-copy{position:absolute;left:310px;top:506px;width:450px;font-family:Arial,sans-serif;font-size:8.4px;line-height:13px;color:var(--text)}
.welcome-copy p+p{margin-top:12px}

/* services */
.services{position:absolute;left:0;top:658px;width:903px;height:284px;background:var(--band)}
.card{position:absolute;top:26px;width:200px;height:232px;background:#fff;box-shadow:0 1px 3px rgba(0,0,0,.18);text-align:center}
.card-img{width:200px;height:129px}
.card h3{margin-top:7px;font-size:12px;font-weight:400;color:var(--navy)}
.card p{margin-top:4px;font-size:9.8px;line-height:15.5px;color:var(--text)}
.card .btn{margin-top:8px;width:78px;height:22px;line-height:20px;font-size:9.5px}

/* testimonials */
.section-title{position:absolute;left:0;top:950px;width:903px;text-align:center;font-size:13.5px;color:var(--navy)}
.quote-mark{position:absolute;left:134px;top:982px;font-family:Georgia,serif;font-size:80px;line-height:80px;color:#d0d0d0;font-weight:700}
.quote-copy{position:absolute;left:190px;top:997px;width:565px;text-align:center;font-family:Arial,sans-serif;font-size:8.3px;line-height:13px;color:var(--text)}
.quote-author{position:absolute;left:0;top:1058px;width:903px;text-align:center;font-size:11.5px;color:var(--text)}
.quote-author span{font-family:Arial,sans-serif;font-size:8.3px}

/* footer */
.site-footer{position:absolute;left:0;top:1097px;width:903px;height:77px;background:var(--footer);color:#fff}
.footer-col{position:absolute;top:14px;text-align:center}
.footer-col h4{font-size:11.5px;font-weight:600;letter-spacing:.2px}
.newsletter{left:135px;width:195px}
.newsletter form{position:absolute;top:27px;left:0;display:flex;gap:11px}
.newsletter .field{width:130px;height:19px;background:#fff;border:none;font-size:8px;color:#999;padding:0 6px;font-family:Arial,sans-serif}
.newsletter .submit{width:54px;height:19px;background:var(--navy);color:#fff;border:1px solid #fff;font-size:8.5px;font-family:"Open Sans",Arial,sans-serif}
.contact{left:365px;width:180px}
.contact p{margin-top:14px;font-size:8.5px}
.contact strong{font-size:11px}
.follow{left:580px;width:180px}
.footer-social span{position:absolute;top:38px;width:23px;height:23px;border-radius:50%;background:var(--foot-icon)}
.footer-bottom{position:absolute;left:0;top:1174px;width:903px;height:26px;background:var(--navy-dark);color:#c9d0ea;font-family:Arial,sans-serif;font-size:8px}
.footer-bottom .copy{position:absolute;left:135px;top:8px}
.footer-bottom .legal{position:absolute;right:135px;top:8px}
</style>
</head>
<body>

<header class="site-header">
  <div class="brand"><span class="brand-dot"></span><span class="brand-name">KAIRO<br>Consulting, Inc.</span></div>
  <nav class="main-nav">
    <a href="#" class="active" style="left:332px">Home</a>
    <a href="#" style="left:405px">About Us</a>
    <a href="#" style="left:491px">Our Services</a>
    <a href="#contact" style="left:594px">Contact Us</a>
  </nav>
  <div class="nav-marker"></div>
  <div class="social-top">
    <span aria-label="Social link" style="left:672px;background:var(--fb)"></span>
    <span aria-label="Social link" style="left:708px;background:var(--tw)"></span>
    <span aria-label="Social link" style="left:744px;background:var(--yt)"></span>
  </div>
</header>

<section class="hero" role="img" aria-label="Researcher holding a test tube under a pipette in a blurred lab setting">
  <div class="hero-text">
    <div class="h1">Clinical Research</div>
    <div class="h2">product safety</div>
    <div class="h3">claim development strategy</div>
  </div>
  <a href="#" class="btn">Read More &nbsp;»</a>
</section>
<div class="hero-rule"></div>

<h2 class="welcome-title"><small>Welcome to </small><b>CLINICAL</b> RESEARCH <span class="accent">CONSULTING</span></h2>
<div class="title-rule" style="left:258px;top:496px;width:387px"></div>
<div class="welcome-img" role="img" aria-label="Gloved hands working with sample vials and flasks"></div>
<div class="welcome-copy">
  <p>Lorem ipsum dolor sit amet, consetetur sadipscing elitr, sed diam nonumy eirmod tempor invidunt ut labore et dolore magna aliquyam erat, sed diam voluptua. At vero eos et accusam et justo duo dolores et ea rebum. Stet clita kasd gubergren, no sea takimata sanctus est Lorem ipsum dolor sit amet. Lorem ipsum dolor sit amet, consetetur sadipscing elitr, sed diam nonumy eirmod tempor invidunt ut labore et dolore magna aliquyam erat, sed diam voluptua. At vero eos et accusam et justo duo dolores et ea rebum. Stet clita kasd gubergren, no sea takimata sanctus est Lorem ipsum dolor sit amet.</p>
  <p>Lorem ipsum dolor sit amet, consetetur sadipscing elitr, sed diam nonumy eirmod tempor invidunt ut labore et dolore magna aliquyam erat, sed diam voluptua. At vero eos et accusam et justo duo dolores et ea rebum. Stet clita kasd gubergren, no sea takimata sanctus est Lorem ipsum dolor sit amet.</p>
</div>

<section class="services">
  <article class="card" style="left:135px">
    <div class="card-img" role="img" aria-label="Scientist examining a slide next to a microscope" style="background:linear-gradient(135deg,#6d8fc4,#d9cfc8 60%,#f2ede8)"></div>
    <h3>Product Safety</h3>
    <p>Lorem ipsum dolor sit amet,<br>consetetur sadipscing elitr, sed</p>
    <a href="#" class="btn">Read More &nbsp;»</a>
  </article>
  <article class="card" style="left:351px">
    <div class="card-img" role="img" aria-label="Scientist inspecting a flask of liquid" style="background:linear-gradient(135deg,#3f6fd6,#7fa6ea 55%,#e4e8f2)"></div>
    <h3>Claim Development Strategy</h3>
    <p>Lorem ipsum dolor sit amet,<br>consetetur sadipscing elitr, sed</p>
    <a href="#" class="btn">Read More &nbsp;»</a>
  </article>
  <article class="card" style="left:567px">
    <div class="card-img" role="img" aria-label="Audience seated in a lecture hall facing a speaker" style="background:linear-gradient(180deg,#c8d8e6,#8a8a8a 55%,#3a3230)"></div>
    <h3>Lecture Service</h3>
    <p>Lorem ipsum dolor sit amet,<br>consetetur sadipscing elitr, sed</p>
    <a href="#" class="btn">Read More &nbsp;»</a>
  </article>
</section>

<h2 class="section-title" style="font-weight:400">Testimonials</h2>
<div class="title-rule" style="left:252px;top:971px;width:399px"></div>
<div class="quote-mark">“</div>
<blockquote class="quote-copy">Lorem ipsum dolor sit amet, consetetur sadipscing elitr, sed diam nonumy eirmod tempor invidunt ut labore et dolore magna aliquyam erat, sed diam voluptua. At vero eos et accusam et justo duo dolores et ea rebum. Stet clita kasd gubergren, no sea takimata sanctus est Lorem ipsum dolor sit amet. Lorem ipsum dolor sit amet, consetetur sadipscing elitr, sed diam nonumy eirmod tempor invidunt ut labore et dolore magna aliquyam erat, sed diam voluptua. At vero eos et accusam et justo duo dolores et ea rebum.</blockquote>
<p class="quote-author">Maren T <span>&nbsp;—&nbsp; CA, United States 18 Feb 2014</span></p>

<footer class="site-footer" id="contact">
  <div class="footer-col newsletter">
    <h4>SUBSRIBE FOR NEWSLETTER</h4>
    <form>
      <input class="field" type="text" placeholder="Enter Email here">
      <button class="submit" type="button">Subscribe</button>
    </form>
  </div>
  <div class="footer-col contact">
    <h4>CONTACT US FOR DETAILS</h4>
    <p>Call Us: <strong>555-013-2468</strong> &nbsp;or&nbsp; <b>EMAIL US »</b></p>
  </div>
  <div class="footer-col follow">
    <h4>FOLLOW US ON SOCIAL MEDIA</h4>
  </div>
  <div class="footer-social">
    <span aria-label="Social link" style="left:605px"></span>
    <span aria-label="Social link" style="left:641px"></span>
    <span aria-label="Social link" style="left:677px"></span>
  </div>
</footer>
<div class="footer-bottom">
  <span class="copy">Copyright © 2015 Company Name. All Rights Reserved.</span>
  <span class="legal">Terms of Service &nbsp;&nbsp;| &nbsp;&nbsp;Privacy Policy</span>
</div>

</body>
</html>
```